Bus Card - T.K. Gate Co
T.K. Gate Co
Project: Bus Card - T.K. Gate Co
Creative Brief
Professional
Owner
4172 Pelton Lane Alder Falls, OH 43950
tkmorrowventures@mailpost.example
Would prefer a design for wooden business cards.

```html
<!DOCTYPE html>
<html lang="en">
<head>
<meta charset="utf-8">
<title>Bus Card - T.K. Gate Co</title>
<link rel="stylesheet" href="https://fonts.googleapis.com/css2?family=Montserrat:wght@400;500;700;800&display=swap">
<style>
  :root {
    --stage: #1a1d21;
    --card: #173a48;
    --card-deep: #122f3b;
    --gold: #f0a11f;
    --gold-light: #f7b733;
    --ink: #14313d;
    --line: #c9d4d6;
    --text: #e6ecec;
  }
  * { box-sizing: border-box; margin: 0; padding: 0; }
  html, body { width: 1200px; height: 901px; overflow: hidden; }
  body {
    background: var(--stage);
    font-family: "Montserrat", sans-serif;
    position: relative;
  }
  .card {
    position: absolute;
    left: 100px; top: 165px;
    width: 1000px; height: 571px;
    background: var(--card);
    overflow: hidden;
    border-radius: 6px;
  }
  .card-grain {
    position: absolute; inset: 0;
    background: radial-gradient(ellipse at 30% 60%, #1c4455 0%, var(--card) 45%, var(--card-deep) 100%);
  }
  .wood-band { position: absolute; left: 0; top: 0; width: 1000px; height: 200px; }
  .name-ribbon {
    position: absolute; left: 560px; top: 62px;
    width: 440px; height: 70px;
    display: flex; align-items: center; padding-left: 50px;
    font-weight: 800; font-size: 40px; color: var(--ink);
    letter-spacing: 0.5px;
  }
  .role-tag {
    position: absolute; left: 790px; top: 140px;
    width: 210px; height: 46px;
    background: var(--gold);
    display: flex; align-items: center; padding-left: 40px;
    font-weight: 500; font-size: 26px; color: var(--text);
    clip-path: polygon(18px 0, 100% 0, 100% 100%, 0 100%);
  }
  .logo-box, .qr-box {
    position: absolute;
    border: 2px solid var(--line);
    display: flex; align-items: center; justify-content: center;
    color: var(--line); font-weight: 500;
  }
  .logo-box { left: 90px; top: 110px; width: 190px; height: 150px; font-size: 26px; letter-spacing: 2px; }
  .qr-box { left: 90px; top: 300px; width: 130px; height: 110px; font-size: 14px; }
  .contact-list {
    position: absolute; left: 560px; top: 240px;
    list-style: none;
  }
  .contact-list li {
    display: flex; align-items: center; gap: 18px;
    height: 44px;
    font-size: 19px; color: var(--text);
  }
  .contact-list li.address { height: 62px; align-items: flex-start; padding-top: 8px; }
  .contact-list svg { width: 22px; height: 22px; flex: none; }
</style>
</head>
<body>
  <div class="card">
    <div class="card-grain" role="img" aria-label="Dark teal wood grain texture"></div>

    <svg class="wood-band" viewBox="0 0 1000 200" role="img" aria-label="Golden wood grain strip">
      <defs>
        <linearGradient id="gold-grain" x1="0" y1="0" x2="1" y2="1">
          <stop offset="0" stop-color="#f7b733"/>
          <stop offset="1" stop-color="#e0901a"/>
        </linearGradient>
      </defs>
      <polygon points="300,0 600,0 560,62 350,40" fill="url(#gold-grain)"/>
      <polygon points="560,62 1000,62 1000,132 540,132" fill="var(--gold)"/>
    </svg>

    <div class="name-ribbon">T.K. Gate Co</div>
    <div class="role-tag">Owner</div>

    <div class="logo-box">LOGO</div>
    <div class="qr-box">QR Code</div>

    <ul class="contact-list">
      <li>
        <svg viewBox="0 0 24 24"><path fill="var(--gold)" d="M6.6 10.8a15 15 0 0 0 6.6 6.6l2.2-2.2c.3-.3.7-.4 1-.2 1.1.4 2.3.6 3.6.6.6 0 1 .4 1 1V20c0 .6-.4 1-1 1C10.6 21 3 13.4 3 4c0-.6.4-1 1-1h3.5c.6 0 1 .4 1 1 0 1.3.2 2.5.6 3.6.1.3 0 .7-.2 1z"/></svg>
        304-555-0142
      </li>
      <li>
        <svg viewBox="0 0 24 24"><rect x="6" y="2" width="12" height="20" rx="2" fill="var(--gold)"/><rect x="8" y="5" width="8" height="12" fill="var(--card)"/></svg>
        877-555-0198
      </li>
      <li class="address">
        <svg viewBox="0 0 24 24"><path fill="var(--gold)" d="M12 2a7 7 0 0 0-7 7c0 5 7 13 7 13s7-8 7-13a7 7 0 0 0-7-7zm0 9.5A2.5 2.5 0 1 1 12 6.5a2.5 2.5 0 0 1 0 5z"/></svg>
        <span>4172 Pelton Lane Alder Falls,<br>OH 43950</span>
      </li>
      <li>
        <svg viewBox="0 0 24 24"><rect x="2" y="5" width="20" height="14" rx="1" fill="var(--gold)"/><path d="M2 6l10 7 10-7" fill="none" stroke="var(--card)" stroke-width="1.6"/></svg>
        tkmorrowventures@mailpost.example
      </li>
    </ul>
  </div>
</body>
</html>
```